IT Consulting company Needs a Logo Design and Business Cards

I need a New Logo and Business Cards for an established IT Managed Services Company that specializes in flat-rate managed IT services. We provide Design and Build, Help Desk, Onsite and Remote Support Services.

Target Market(s)

Corporate Clients

Industry/Entity Type

It Company

Logo Text

Halbrook Computer Group

Requirements
Nice to have
• Tag Line= Technology at Lightning Speed

```html
<!DOCTYPE html>
<html lang="en">
<head>
<meta charset="UTF-8">
<title>Halbrook Computer Group – Business Cards</title>
<link href="https://fonts.googleapis.com/css2?family=Open+Sans:wght@400;600&display=swap" rel="stylesheet">
<style>
  :root {
    --page-bg: #d9d6d1;
    --card-dark: #000000;
    --card-light: #222222;
    --brand-blue: #3f78c4;
    --text-grey: #b9b9b9;
    --text-light: #cfcfcf;
  }
  * { box-sizing: border-box; margin: 0; padding: 0; }
  html, body {
    width: 1200px;
    height: 900px;
    overflow: hidden;
  }
  body {
    background: var(--page-bg);
    font-family: "Open Sans", Arial, sans-serif;
    display: flex;
    flex-direction: column;
    align-items: center;
    justify-content: center;
    gap: 40px;
  }
  .card {
    width: 680px;
    height: 389px;
    background: linear-gradient(160deg, var(--card-dark) 35%, var(--card-light) 100%);
    box-shadow: 0 10px 24px rgba(0,0,0,0.35);
    position: relative;
  }
  .brand {
    display: flex;
    align-items: center;
    gap: 12px;
  }
  .brand-square {
    width: 18px;
    height: 18px;
    background: var(--brand-blue);
    flex-shrink: 0;
  }
  .brand-name {
    color: var(--text-grey);
    font-weight: 600;
    line-height: 1.1;
  }

  /* Front */
  .card-front {
    display: flex;
    align-items: center;
    justify-content: center;
  }
  .card-front .brand-name { font-size: 34px; }

  /* Back */
  .card-back .brand {
    position: absolute;
    left: 44px;
    top: 158px;
    width: 250px;
  }
  .card-back .brand-name { font-size: 24px; }
  .divider {
    position: absolute;
    left: 330px;
    top: 110px;
    width: 2px;
    height: 180px;
    background: var(--brand-blue);
  }
  .contact {
    position: absolute;
    left: 368px;
    top: 110px;
    color: var(--text-light);
  }
  .contact-name {
    font-size: 26px;
    font-weight: 400;
    letter-spacing: 0.5px;
    line-height: 1;
  }
  .contact-role {
    color: var(--brand-blue);
    font-size: 17px;
    margin-bottom: 18px;
  }
  .contact-list {
    list-style: none;
    font-size: 17px;
  }
  .contact-list li {
    display: flex;
    align-items: center;
    gap: 10px;
    height: 30px;
  }
  .contact-icon {
    width: 16px;
    height: 16px;
    fill: none;
    stroke: var(--brand-blue);
    stroke-width: 1.6;
  }
  .contact-address { margin-top: 4px; }
</style>
</head>
<body>
  <section class="card card-front">
    <div class="brand">
      <span class="brand-square"></span>
      <span class="brand-name">Halbrook Computer Group</span>
    </div>
  </section>

  <section class="card card-back">
    <div class="brand">
      <span class="brand-square"></span>
      <span class="brand-name">Halbrook Computer Group</span>
    </div>
    <div class="divider"></div>
    <div class="contact">
      <p class="contact-name">YOUR NAME</p>
      <p class="contact-role">Owner</p>
      <ul class="contact-list">
        <li>
          <svg class="contact-icon" viewBox="0 0 16 16" aria-hidden="true"><path d="M4 1.5 L6.5 4 L5 6 C6 8.5 7.5 10 10 11 L12 9.5 L14.5 12 L12.5 14.5 C7 14 2 9 1.5 3.5 Z"/></svg>
          <span>000 000 0000</span>
        </li>
        <li>
          <svg class="contact-icon" viewBox="0 0 16 16" aria-hidden="true"><rect x="1.5" y="3.5" width="13" height="9"/><path d="M1.5 3.5 L8 9 L14.5 3.5"/></svg>
          <span>youremail@xyz.com</span>
        </li>
        <li>
          <svg class="contact-icon" viewBox="0 0 16 16" aria-hidden="true"><circle cx="8" cy="8" r="6.5"/><ellipse cx="8" cy="8" rx="3" ry="6.5"/><path d="M1.5 8 H14.5"/></svg>
          <span>www.yourwebsite.com</span>
        </li>
        <li class="contact-address"><span>Your Address here</span></li>
      </ul>
    </div>
  </section>
</body>
</html>
```